New Business Cards for Torvin Group

We need a new Business Card to compliment our new logo. We are a vibrant design, manufacture and install business providing recreation areas, public parks and Municipal spaces. We want business cards that are classy, modern and clean.

We have recently changed our logo, and are celebrating our 40th anniversary. We want business cards with a new modern design to reflect our status.

Target Market(s)

Customers

Contact Information for Business Card

We need all the details of our 3 offices as per the business card attached. Please disregard the old logo on the business card, the other three files show our new logo.

Requirements
Must have
• All info as per attached business card but with new logo.
Nice to have

```html
<!DOCTYPE html>
<html lang="en">
<head>
<meta charset="utf-8">
<title>Torvin Group – Business Card</title>
<link href="https://fonts.googleapis.com/css2?family=Barlow:wght@400;500;600;700&display=swap" rel="stylesheet">
<style>
  :root {
    --brand-red: #e8303a;
    --charcoal: #4a4a4f;
    --body-grey: #555558;
    --card-white: #ffffff;
    --backdrop: #e9e6e2;
  }
  * { margin: 0; padding: 0; box-sizing: border-box; }
  html, body {
    width: 1200px; height: 989px; overflow: hidden;
    background: var(--backdrop);
    font-family: "Barlow", Arial, sans-serif;
  }
  .card {
    position: absolute; left: 50px; top: 180px;
    width: 1100px; height: 637px;
    background: var(--card-white);
    box-shadow: 0 6px 18px rgba(0,0,0,0.18);
    overflow: hidden;
  }
  .name-band {
    position: absolute; left: 0; top: 127px;
    width: 472px; height: 97px;
    background: var(--charcoal);
    clip-path: polygon(0 0, 395px 0, 472px 97px, 0 97px);
    color: #fff;
    padding: 10px 0 0 51px;
  }
  .name-band .person-name { font-size: 40px; font-weight: 700; letter-spacing: 0.5px; line-height: 46px; }
  .name-band .person-title { font-size: 25px; font-weight: 400; letter-spacing: 0.5px; line-height: 30px; }

  .brand {
    position: absolute; left: 700px; top: 110px;
    display: flex; align-items: center; gap: 22px;
  }
  .brand .brand-dot {
    width: 110px; height: 110px; border-radius: 50%;
    background: var(--brand-red);
  }
  .brand .brand-name {
    font-size: 46px; font-weight: 700; color: var(--charcoal);
    line-height: 1.0; letter-spacing: 1px; width: 220px;
  }

  .office {
    position: absolute; top: 366px;
    color: var(--body-grey);
  }
  .office.head { left: 51px; }
  .office.dubai { left: 399px; }
  .office.qatar { left: 752px; }
  .office h2 {
    color: var(--brand-red); font-size: 25px; font-weight: 600;
    line-height: 30px; margin-bottom: 10px;
  }
  .office .address { font-size: 24px; line-height: 30px; margin-bottom: 10px; letter-spacing: 0.4px; }
  .office .line {
    display: flex; align-items: center; gap: 12px;
    font-size: 24px; line-height: 34px; letter-spacing: 0.3px;
  }
  .office .line svg { width: 24px; height: 20px; flex: none; fill: var(--brand-red); }

  .contact-bar {
    position: absolute; left: 0; bottom: 0; width: 100%; height: 55px;
    background: var(--brand-red); color: #fff;
    font-size: 24px; font-weight: 400; letter-spacing: 0.4px;
    display: flex; align-items: center; justify-content: center;
  }
</style>
</head>
<body>
<svg width="0" height="0" style="position:absolute">
  <defs>
    <symbol id="icon-phone" viewBox="0 0 24 24"><path d="M6.6 2.5l3 3.2-1.8 2.6c1.3 2.8 3.4 5 6.2 6.4l2.6-1.8 3.3 3-1.6 3.4c-8.6-0.4-15.3-7.4-15.4-15.6z"/></symbol>
    <symbol id="icon-fax" viewBox="0 0 24 20"><rect x="6" y="1" width="12" height="7"/><rect x="1" y="9" width="22" height="6" rx="1"/><rect x="3" y="16" width="18" height="3"/></symbol>
    <symbol id="icon-mail" viewBox="0 0 24 18"><path d="M1 2h22v14H1z M1 2l11 8 11-8" fill="none" stroke="#e8303a" stroke-width="0"/><path d="M1 1h22v2L12 10 1 3z M1 5l11 7.5L23 5v12H1z"/></symbol>
  </defs>
</svg>

<main class="card">
  <header class="name-band">
    <div class="person-name">Marek Delavane</div>
    <div class="person-title">Managing Partner</div>
  </header>

  <div class="brand">
    <div class="brand-dot"></div>
    <div class="brand-name">TORVIN GROUP</div>
  </div>

  <section class="office head">
    <h2>Head office</h2>
    <p class="address">41820 Abu Dhabi, U.A.E</p>
    <p class="line"><svg><use href="#icon-phone"/></svg>+971 (0)2 5318207</p>
    <p class="line"><svg><use href="#icon-fax"/></svg>+971 (0)2 5318208</p>
    <p class="line"><svg><use href="#icon-mail"/></svg>sales@torvingroup.com</p>
  </section>

  <section class="office dubai">
    <h2>Dubai Office</h2>
    <p class="address">508142 Dubai, U.A.E.</p>
    <p class="line"><svg><use href="#icon-phone"/></svg>+971 (0)4 6290354</p>
    <p class="line"><svg><use href="#icon-fax"/></svg>+971(0)4 6290377</p>
    <p class="line"><svg><use href="#icon-mail"/></svg>sales@torvingroup.com</p>
  </section>

  <section class="office qatar">
    <h2>Qatar Office</h2>
    <p class="address">27390 Doha, Qatar</p>
    <p class="line"><svg><use href="#icon-phone"/></svg>+974 47215830</p>
    <p class="line"><svg><use href="#icon-fax"/></svg>+974 47936142</p>
    <p class="line"><svg><use href="#icon-mail"/></svg>sales@torvingroup.com</p>
  </section>

  <footer class="contact-bar">
    P. +971 (0)50 784 3906&nbsp; E.marek@torvingroup.com&nbsp; W. www.torvingroup.com
  </footer>
</main>
</body>
</html>
```